Brimovex business card

Based on company logo and website given , to design a business card temple. Slogan "Your furry friends deserves the best"
Color style please refer to our website

```html
<!DOCTYPE html>
<html lang="en">
<head>
<meta charset="utf-8">
<title>Brimovex Stationery</title>
<link rel="stylesheet" href="https://fonts.googleapis.com/css2?family=Montserrat:wght@300;400;500;600&display=swap">
<style>
  :root {
    --backdrop: #aaa8a9;
    --paper: #ffffff;
    --brand-blue: #2069b4;
    --ink: #555a60;
    --ink-dark: #3d4248;
    --shadow: 3px 4px 6px rgba(0,0,0,0.35);
  }
  * { margin: 0; padding: 0; box-sizing: border-box; }
  html, body { width: 1200px; height: 764px; overflow: hidden; }
  body {
    background: var(--backdrop);
    font-family: "Montserrat", sans-serif;
    color: var(--ink);
    position: relative;
  }
  .sheet { position: absolute; background: var(--paper); box-shadow: var(--shadow); }
  .wordmark {
    position: absolute;
    font-family: "Montserrat", sans-serif;
    font-weight: 600;
    color: var(--brand-blue);
    letter-spacing: -0.5px;
    white-space: nowrap;
    transform: translateX(-50%);
    line-height: 1;
  }
  .wordmark--light { color: var(--paper); }

  /* Letterhead */
  .letterhead { left: 59px; top: 60px; width: 455px; height: 644px; }
  .letterhead .wordmark { left: 227px; top: 58px; font-size: 38px; }
  .letter-text {
    position: absolute; left: 41px; width: 373px;
    font-size: 7.5px; font-weight: 300; letter-spacing: -0.08px;
    line-height: 12.5px; color: var(--ink-dark);
  }
  .letter-greeting { top: 163px; }
  .letter-body { top: 188px; text-align: justify; }
  .letter-body p { margin-bottom: 12.5px; }
  .letter-signoff { top: 462px; }
  .signature-area {
    position: absolute; left: 41px; top: 488px; width: 54px; height: 50px;
    background: #eef1f5; border-radius: 3px;
  }
  .letter-footer {
    position: absolute; left: 72px; top: 591px;
    display: flex; font-size: 8.3px; line-height: 11px; color: var(--ink);
  }
  .footer-col { padding: 0 7px; border-left: 1px solid #8a8f96; }
  .footer-col:first-child { border-left: none; padding-left: 0; }
  .icon-line { display: flex; align-items: center; gap: 3px; }
  .icon-line svg { width: 7px; height: 7px; fill: var(--brand-blue); flex: none; }

  /* Business cards */
  .card { top: 152px; width: 268px; height: 153px; }
  .card-front { left: 584px; }
  .card-front .wordmark { left: 75px; top: 64px; font-size: 22px; }
  .card-divider {
    position: absolute; left: 138px; top: 43px; width: 1px; height: 66px;
    background: var(--brand-blue);
  }
  .card-details { position: absolute; left: 148px; top: 43px; font-size: 6.2px; line-height: 8.6px; }
  .card-name { color: var(--brand-blue); font-size: 7.6px; font-weight: 500; letter-spacing: 0.2px; line-height: 9px; }
  .card-role { color: var(--ink-dark); font-weight: 500; margin-bottom: 5px; }
  .card-details .icon-line svg { width: 5.5px; height: 5.5px; }

  .card-back { left: 861px; background: var(--brand-blue); }
  .card-back .wordmark { left: 134px; top: 64px; font-size: 34px; }
  .card-slogan {
    position: absolute; left: 0; width: 100%; top: 127px; text-align: center;
    color: var(--paper); font-size: 6.6px; font-weight: 500; letter-spacing: 0.2px;
  }

  /* Envelopes */
  .envelope-back { left: 587px; top: 321px; width: 548px; height: 255px; }
  .envelope-flap { position: absolute; left: 0; top: 0; }
  .envelope-back .wordmark { left: 273px; top: 32px; font-size: 28px; }

  .envelope-front { left: 545px; top: 449px; width: 548px; height: 255px; }
  .envelope-front .wordmark { left: 95px; top: 49px; font-size: 28px; }
  .return-address {
    position: absolute; left: 95px; top: 84px; transform: translateX(-50%);
    text-align: center; font-size: 8.5px; line-height: 10.5px; white-space: nowrap;
  }
</style>
</head>
<body>

  <section class="sheet letterhead">
    <div class="wordmark">Brimovex</div>
    <p class="letter-text letter-greeting">Dear customer,</p>
    <div class="letter-text letter-body">
      <p>Lorem ipsum dolor sit amet, consectetur adipisicing elit, sed do eiusmod tempor incididunt ut labore et dolore magna aliqua. Ut enim ad minim veniam, quis nostrud exercitation ullamco laboris nisi ut aliquip ex ea commodo consequat. Duis aute irure dolor in reprehenderit in voluptate velit esse cillum dolore eu fugiat nulla pariatur. Excepteur sint occaecat cupidatat non proident, sunt in culpa qui officia deserunt mollit anim id est laborum.</p>
      <p>Lorem ipsum dolor sit amet, consectetur adipisicing elit, sed do eiusmod tempor incididunt ut labore et dolore magna aliqua. Ut enim ad minim veniam, quis nostrud exercitation ullamco laboris nisi ut aliquip ex ea commodo consequat. Duis aute irure dolor in reprehenderit in voluptate velit esse cillum dolore eu fugiat nulla pariatur. Excepteur sint occaecat cupidatat non proident, sunt in culpa qui officia deserunt mollit anim id est laborum.</p>
      <p>Lorem ipsum dolor sit amet, consectetur adipisicing elit, sed do eiusmod tempor incididunt ut labore et dolore magna aliqua. Ut enim ad minim veniam, quis nostrud exercitation ullamco laboris nisi ut aliquip ex ea commodo consequat. Duis aute irure dolor in reprehenderit in voluptate velit esse cillum dolore eu fugiat nulla pariatur. Excepteur sint occaecat cupidatat non proident, sunt in culpa qui officia deserunt mollit anim id est laborum.</p>
      <p>Lorem ipsum dolor sit amet, consectetur adipisicing elit, sed do eiusmod tempor incididunt ut labore et dolore magna aliqua. Ut enim ad minim veniam, quis nostrud exercitation ullamco laboris nisi ut aliquip ex ea commodo consequat. Duis aute irure dolor in reprehenderit.</p>
    </div>
    <p class="letter-text letter-signoff">Yours Sincerely,</p>
    <div class="signature-area" role="img" aria-label="Handwritten signature"></div>
    <div class="letter-footer">
      <div class="footer-col">
        <div class="icon-line"><svg viewBox="0 0 10 10"><path d="M2 0.5l2 2-1 1.3c.6 1.3 1.6 2.3 2.9 2.9l1.3-1 2 2-1.2 1.8C4.5 9.3.7 5.5.2 1.7z"/></svg>+56910473326</div>
        <div class="icon-line"><svg viewBox="0 0 10 10"><rect x="2.5" y="0.5" width="5" height="3"/><rect x="0.5" y="3.5" width="9" height="4" rx="1"/><rect x="2.5" y="6.5" width="5" height="3"/></svg>+56910473326</div>
      </div>
      <div class="footer-col">
        <div class="icon-line"><svg viewBox="0 0 10 10"><rect x="0.5" y="2" width="9" height="6.5"/><path d="M0.5 2l4.5 3.5L9.5 2" fill="none" stroke="#fff" stroke-width="0.9"/></svg>hello@norvatile.com</div>
        <div class="icon-line"><svg viewBox="0 0 10 10"><circle cx="5" cy="5" r="4.2" fill="none" stroke="var(--brand-blue)" stroke-width="1.2"/><path d="M1 5h8M5 1v8" stroke="var(--brand-blue)" stroke-width="0.8"/></svg>www.norvatile.com</div>
      </div>
      <div class="footer-col">
        <div>48 Harlow Bend Road, Land</div>
        <div>Maple Ridge, ON L7K 3P4</div>
      </div>
    </div>
  </section>

  <section class="sheet card card-front">
    <div class="wordmark">Brimovex</div>
    <div class="card-divider"></div>
    <div class="card-details">
      <div class="card-name">DORIAN VELL ASKER</div>
      <div class="card-role">Managing Director</div>
      <div>48 Harlow Bend Road,</div>
      <div>Maple Ridge, ON L7K 3P4</div>
      <div class="icon-line"><svg viewBox="0 0 10 10"><path d="M2 0.5l2 2-1 1.3c.6 1.3 1.6 2.3 2.9 2.9l1.3-1 2 2-1.2 1.8C4.5 9.3.7 5.5.2 1.7z"/></svg>+56910473326</div>
      <div class="icon-line"><svg viewBox="0 0 10 10"><rect x="0.5" y="2" width="9" height="6.5"/><path d="M0.5 2l4.5 3.5L9.5 2" fill="none" stroke="#fff" stroke-width="0.9"/></svg>info@brimovex.com</div>
      <div class="icon-line"><svg viewBox="0 0 10 10"><circle cx="5" cy="5" r="4.2" fill="none" stroke="var(--brand-blue)" stroke-width="1.2"/><path d="M1 5h8M5 1v8" stroke="var(--brand-blue)" stroke-width="0.8"/></svg>www.brimovex.com</div>
    </div>
  </section>

  <section class="sheet card card-back">
    <div class="wordmark wordmark--light">Brimovex</div>
    <div class="card-slogan">YOUR FURRY FRIENDS DESERVES THE BEST</div>
  </section>

  <section class="sheet envelope-back">
    <svg class="envelope-flap" width="548" height="80" viewBox="0 0 548 80">
      <path d="M0 0H548L534 70Q532 79 522 79H26Q16 79 14 70Z" fill="var(--brand-blue)"/>
    </svg>
    <div class="wordmark wordmark--light">Brimovex</div>
  </section>

  <section class="sheet envelope-front">
    <div class="wordmark">Brimovex</div>
    <div class="return-address">48 Harlow Bend Road,<br>Maple Ridge, ON L7K 3P4</div>
  </section>

</body>
</html>
```